Homepage design for personal injury lawyer

NOTE: I will not close the project until June 9th. I want to give everyone time to put in their best work.
Your task is to redesign the homepage for this site:
https://corwistlane.com/
Feel free to use any images you find on the site.
I'm deliberately leaving the description simple so that I don't limit you.
Updates
Hi everyone. I will keep the project open for a few days to leave time for designs.
Number of Pages Required
1 page
Look and feel
Each slider illustrates characteristics of the customer's brand and the style your logo design should communicate.

```html
<!DOCTYPE html>
<html lang="en">
<head>
<meta charset="utf-8">
<title>Corwist Lane Injury Lawyers – Phoenix Personal Injury Lawyers</title>
<link href="https://fonts.googleapis.com/css2?family=Oswald:wght@400;500;600&family=Mulish:wght@400;600;700&display=swap" rel="stylesheet">
<style>
:root{
  --blue:#1b56a5;
  --blue-dark:#0f3f82;
  --blue-soft:#e3ebf5;
  --grey-bg:#eeeff2;
  --canvas:#e7e7e8;
  --ink:#2b2f36;
  --muted:#5b616b;
  --line:#d7dbe1;
  --white:#ffffff;
  --black:#050505;
}
*{box-sizing:border-box;margin:0;padding:0}
html,body{width:1200px;height:2264px;overflow:hidden;background:var(--canvas)}
body{font-family:"Mulish",sans-serif;color:var(--ink)}
.stage{position:absolute;left:0;top:0;width:1365px;height:2576px;transform:scale(0.87912);transform-origin:0 0;background:var(--canvas)}
.col{position:absolute;width:552px;background:var(--white);box-shadow:0 2px 8px rgba(0,0,0,.06);overflow:hidden}
.col-left{left:91px;top:100px;height:2376px}
.col-right{left:723px;top:100px;height:2306px}
section,header{position:relative;width:552px}
.abs{position:absolute}
.h{font-family:"Oswald",sans-serif;font-weight:500;color:var(--blue);letter-spacing:.1px}
.h .lt{color:#3d4a5c;font-weight:400}
.center{text-align:center}
.p{font-size:6.3px;line-height:1.75;color:var(--muted)}
.btn{position:absolute;background:var(--blue);color:#fff;font-family:"Oswald",sans-serif;font-weight:500;font-size:7.5px;display:flex;align-items:center;justify-content:center}
.btn-ghost{background:transparent;border:1px solid #fff}
.ph{position:absolute}
.icon-c{position:absolute;border-radius:50%;border:2px solid var(--blue);display:flex;align-items:center;justify-content:center;background:#fff}

/* top bar & nav */
.topbar{height:20px;background:var(--blue);color:#fff;font-size:7px;display:flex;align-items:center;justify-content:center;gap:4px}
.topbar b{font-size:8px}
.nav{height:36px;display:flex;align-items:center;padding-left:48px}
.brand{display:flex;align-items:center;gap:5px}
.brand-dot{width:20px;height:20px;border-radius:50%;background:var(--blue)}
.brand-name{font-family:"Oswald",sans-serif;font-size:11.5px;color:var(--blue);line-height:1}
.brand-sub{font-size:4.6px;letter-spacing:3px;color:var(--muted);margin-top:2px}
.menu{display:flex;gap:11px;margin-left:46px;font-family:"Oswald",sans-serif;font-size:7px;color:#222}
.menu .on{background:var(--blue-soft);color:var(--blue);padding:1px 6px;border-radius:6px}

/* hero */
.hero{height:264px;background:var(--white)}
.hero-photo{left:0;top:0;width:552px;height:240px;background:linear-gradient(100deg,#1c3f6e 0%,#3c5a7e 38%,#7c8a98 60%,#a9a6a0 100%)}
.hero h1{position:absolute;left:47px;top:42px;font-family:"Oswald",sans-serif;font-weight:500;font-size:25px;line-height:1.2;color:#fff}
.checks{position:absolute;left:47px;top:110px;list-style:none;color:#fff;font-size:8.4px;line-height:2.4}
.checks li{display:flex;align-items:center;gap:5px}
.tick{width:8px;height:8px;border:1px solid #fff;border-radius:50%;display:inline-block;position:relative}
.tick:after{content:"";position:absolute;left:2px;top:1px;width:2px;height:3.5px;border:solid #fff;border-width:0 1px 1px 0;transform:rotate(45deg)}

/* media */
.media{height:110px}
.media h3{font-size:9.5px;color:#222;top:34px;width:100%}
.media-row{position:absolute;top:61px;left:86px;display:flex;gap:10px;align-items:center}
.mark{width:22px;height:22px;border-radius:50%;background:#c9ced6}
.mark.sq{border-radius:3px}
.mark.wide{width:84px;height:8px;border-radius:2px;background:#9aa0a8}

/* helping */
.helping{height:240px;background:var(--grey-bg)}

/* features */
.why{height:260px}
.feat h4{font-family:"Oswald",sans-serif;font-weight:500;font-size:8.5px;color:#222}
.feat .p{width:160px;margin-top:3px}

/* recovered */
.recovered{height:315px}
.stat h4{font-family:"Oswald",sans-serif;font-weight:500;font-size:8.5px;color:#fff}
.stat .amt{font-family:"Oswald",sans-serif;font-size:14.5px;color:#fff;margin-top:2px}
.stat .p{color:#dbe6f5;margin-top:8px}

/* services */
.services{height:425px}
.card{position:absolute;width:147px;height:115px;border-radius:7px;overflow:hidden}
.card span{position:absolute;left:0;right:0;bottom:12px;text-align:center;color:#fff;font-family:"Oswald",sans-serif;font-size:8px}
.link{color:var(--blue)}

/* partnering */
.partner{height:410px}
.steps-list{position:absolute;left:47px;top:118px;width:200px;border:1px solid var(--line);background:#fff}
.step{height:43px;display:flex;align-items:center;gap:9px;padding-left:9px;border-bottom:1px solid var(--line);font-size:6.6px;font-weight:700;color:#222}
.step .ic{width:23px;height:23px;border-radius:50%;background:var(--blue);flex:none}
.step.active{background:var(--blue);color:#fff;height:46px}
.step.active .ic{background:#fff}
.step small{display:block;font-weight:400;font-size:5px;line-height:1.5;margin-top:2px}

/* faq */
.faq{height:296px}
.pill{position:absolute;width:222px;height:30px;border:1px solid var(--line);border-radius:8px;font-size:5.8px;line-height:1.5;color:#333;display:flex;align-items:center;padding:0 26px 0 12px;box-shadow:0 1px 3px rgba(0,0,0,.05)}
.pill:after{content:"";position:absolute;right:10px;top:12px;width:5px;height:5px;border-radius:50%;border:1.5px solid var(--blue)}

/* right column */
.consult{height:210px}
.cstat{position:absolute;top:83px;display:flex;align-items:center;gap:8px;color:#fff;font-size:8px}
.cstat .ring{width:30px;height:30px;border-radius:50%;border:2px solid #fff;background:rgba(255,255,255,.12)}
.firm{height:280px}
.bio{position:absolute;left:57px;top:143px;width:437px;height:93px;border:1.5px solid var(--blue);border-radius:9px}
.tag{position:absolute;background:var(--blue);color:#fff;font-size:6px;font-weight:700;padding:3px 10px;border-radius:8px}
.named{height:233px;background:var(--blue-soft)}
.roadmap{height:327px}
.rm-label{position:absolute;width:80px;text-align:center;font-size:6.2px;line-height:1.55;color:#333}
.rm-ring{position:absolute;width:46px;height:46px;border-radius:50%;border:3px solid #777;background:#fff}
.rm-ring.blue{border-color:var(--blue)}
.serving{height:485px;background:var(--grey-bg)}
.circle-img{position:absolute;border-radius:50%;border:3px solid var(--blue)}
.case{height:235px}
.field{position:absolute;height:20px;border:1px solid #e2e5ea;background:#fff;font-size:5.6px;color:#777;padding:6px 7px;box-shadow:0 1px 4px rgba(0,0,0,.06)}
.footer{height:246px;background:var(--black);color:#fff}
.fcol h5{font-family:"Mulish",sans-serif;font-weight:700;font-size:8px;margin-bottom:7px}
.fcol li{list-style:none;font-size:5.8px;line-height:2.03;color:#ddd}
.fcol li:before{content:"→ ";color:#fff}
.contact-row{display:flex;gap:8px;align-items:flex-start;font-size:5.8px;line-height:1.6;color:#ddd;margin-bottom:10px}
.contact-row i{width:13px;height:13px;border-radius:50%;background:var(--blue);flex:none}
</style>
</head>
<body>
<div class="stage">

<!-- ================= LEFT COLUMN ================= -->
<div class="col col-left">
  <div class="topbar">
    <svg width="7" height="7" viewBox="0 0 10 10"><path d="M2 1l2 2-1 1.5c.6 1.2 1.4 2 2.5 2.5L7 6l2 2-1.5 1.5C4.5 9 1 5.5.5 2.5z" fill="#fff"/></svg>
    Call 24/7 for Free Consultation <b>602-555-0148</b>
  </div>
  <header class="nav">
    <div class="brand">
      <span class="brand-dot"></span>
      <div><div class="brand-name">CORWIST LANE</div><div class="brand-sub">INJURY LAWYERS</div></div>
    </div>
    <nav class="menu">
      <span class="on">Home</span><span>About Us ▾</span><span>Cases We Handle ▾</span><span>Locations ▾</span><span>Resources ▾</span><span>Contact Us</span>
    </nav>
  </header>

  <section class="hero">
    <div class="ph hero-photo" role="img" aria-label="Smiling lead attorney in a grey suit and yellow tie standing in a bright office"></div>
    <svg class="abs" style="left:0;top:190px" width="552" height="74" viewBox="0 0 552 74">
      <path d="M0 30 Q260 90 552 40 L552 74 L0 74Z" fill="#fff"/>
      <path d="M120 66 Q360 62 552 40 L552 46 Q360 70 120 68Z" fill="#1b56a5"/>
      <path d="M0 30 Q260 88 552 32" fill="none" stroke="#2f6fc2" stroke-width="2"/>
    </svg>
    <h1>Phoenix Personal<br>Injury Lawyers</h1>
    <ul class="checks">
      <li><span class="tick"></span>99% Success Rate</li>
      <li><span class="tick"></span>550+ 5-Star Reviews</li>
      <li><span class="tick"></span>$0 Fee Unless We Win</li>
    </ul>
    <div class="btn btn-ghost" style="left:47px;top:176px;width:100px;height:20px">Get Your Free Consultation</div>
  </section>

  <section class="media">
    <h3 class="h abs center" style="color:#222">We are the legal experts the media calls</h3>
    <div class="media-row">
      <span class="mark"></span><span class="mark"></span><span class="mark sq"></span><span class="mark sq"></span><span class="mark sq"></span><span class="mark"></span><span class="mark"></span><span class="mark"></span><span class="mark wide"></span>
    </div>
  </section>

  <section class="helping">
    <div class="abs" style="left:79px;top:41px;width:185px;height:150px;border:1.5px solid var(--blue)"></div>
    <div class="ph" style="left:55px;top:47px;width:202px;height:150px;background:linear-gradient(135deg,#5c6f86,#a8b4c2 55%,#6a5d52)" role="img" aria-label="Three attorneys walking through a glass office lobby"></div>
    <h2 class="h abs" style="left:290px;top:41px;font-size:12.5px;line-height:1.5">Helping Injury Victims Across Phoenix<br><span class="lt">and the Valley Recover and Rebuild</span></h2>
    <p class="p abs" style="left:290px;top:90px;width:212px">Every year, thousands of people in Phoenix and across the Valley suffer serious injuries due to preventable accidents — from unsafe property conditions and workplace incidents to defective products, medical malpractice, and dog bites. Many victims never pursue the compensation they're entitled to. At Corwist Lane Injury Lawyers, our personal injury attorneys help clients throughout Phoenix, Scottsdale, Mesa, and beyond take the first step toward justice and recovery.</p>
    <div class="btn" style="left:290px;top:179px;width:52px;height:19px">Read More</div>
  </section>

  <section class="why">
    <h2 class="h abs center" style="width:100%;top:38px;font-size:12.5px">Why We're Phoenix's Top-Rated <span class="lt">Personal Injury Law Firm</span></h2>
    <p class="p abs center" style="left:68px;top:68px;width:416px">As a distinguished division of Halbrook Ardent, P.C.—Arizona's oldest law firm, established in 1885—our Phoenix legal team carries a level of institutional credibility that few others can match. Over generations, Halbrook Ardent has built trusted relationships with judges, juries, and legal professionals across Maricopa County, earning a reputation for integrity, excellence, and results.</p>
    <div class="icon-c" style="left:56px;top:115px;width:34px;height:34px"><svg width="14" height="14"><circle cx="7" cy="7" r="5" fill="none" stroke="#1b56a5" stroke-width="1.4"/></svg></div>
    <div class="feat abs" style="left:102px;top:114px"><h4>Millions Recovered</h4><p class="p">Our Phoenix personal injury lawyers have secured substantial verdicts and settlements across Arizona in complex injury claims</p></div>
    <div class="icon-c" style="left:292px;top:115px;width:34px;height:34px;border-color:#777"><svg width="14" height="14"><rect x="3" y="3" width="8" height="8" fill="none" stroke="#777" stroke-width="1.4"/></svg></div>
    <div class="feat abs" style="left:339px;top:114px"><h4>99% Success Rate</h4><p class="p">Our track record speaks volumes. From the settlement table to courtroom, we deliver results.</p></div>
    <div class="icon-c" style="left:56px;top:180px;width:34px;height:34px"><svg width="14" height="14"><circle cx="7" cy="5" r="3" fill="none" stroke="#1b56a5" stroke-width="1.4"/><path d="M2 13c1-4 9-4 10 0" fill="none" stroke="#1b56a5" stroke-width="1.4"/></svg></div>
    <div class="feat abs" style="left:102px;top:179px"><h4>Client-Focused Approach</h4><p class="p">Our injury attorneys serve Phoenix and the surrounding areas with compassion, communication, and transparency at every step.</p></div>
    <div class="icon-c" style="left:292px;top:180px;width:34px;height:34px;border-color:#777"><svg width="14" height="14"><path d="M2 8l3 3 7-8" fill="none" stroke="#777" stroke-width="1.4"/></svg></div>
    <div class="feat abs" style="left:339px;top:179px"><h4>No-Fee Promise</h4><p class="p">You never pay unless we win — our no-fee promise applies to all personal injury cases across Phoenix, Scottsdale, Mesa, and beyond.</p></div>
  </section>

  <section class="recovered">
    <svg class="abs" style="left:0;top:0" width="552" height="315" viewBox="0 0 552 315">
      <path d="M0 28 Q276 -4 552 28 L552 270 Q276 340 0 270Z" fill="#1b56a5"/>
    </svg>
    <h2 class="h abs center" style="width:100%;top:46px;font-size:12.5px;color:#fff">Over $100,000,000 Recovered For Personal Injury Victims</h2>
    <p class="abs center" style="width:100%;top:81px;font-size:6.6px;line-height:1.7;color:#e4ecf7">How Much Is Your Case Worth?<br>Discuss With A Personal Injury Lawyer in Phoenix And Find Out Now</p>
    <div class="abs" style="left:195px;top:140px;width:1px;height:75px;background:#9fbbe2"></div>
    <div class="abs" style="left:356px;top:140px;width:1px;height:75px;background:#9fbbe2"></div>
    <div class="stat abs center" style="left:40px;top:116px;width:160px">
      <div style="width:34px;height:34px;border-radius:50%;border:1.5px solid #fff;margin:0 auto 10px"></div>
      <h4>Car Accident</h4><div class="amt">$5,400,000</div><p class="p">Auto accident.<br>Severe limb damage.</p>
    </div>
    <div class="stat abs center" style="left:196px;top:116px;width:160px">
      <div style="width:34px;height:34px;border-radius:50%;border:1.5px solid #fff;margin:0 auto 10px"></div>
      <h4>Commercial Truck Accident</h4><div class="amt">$9,000,000</div><p class="p">Head on collision.<br>Triple fatality.</p>
    </div>
    <div class="stat abs center" style="left:346px;top:116px;width:160px">
      <div style="width:34px;height:34px;border-radius:50%;border:1.5px solid #fff;margin:0 auto 10px"></div>
      <h4>Premises liability</h4><div class="amt">$6,000,000</div><p class="p">Skylight fall injury.<br>Hemiparesis.</p>
    </div>
    <div class="btn btn-ghost" style="left:234px;top:246px;width:84px;height:21px">Call 602-555-0148</div>
  </section>

  <section class="services">
    <h2 class="h abs center" style="width:100%;top:37px;font-size:12.5px">Comprehensive Personal Injury <span class="lt">Services in Phoenix</span></h2>
    <p class="p abs center" style="left:52px;top:70px;width:448px">Each year in Maricopa County, thousands of people are injured in preventable incidents that have nothing to do with traffic collisions. From fall injuries and medical errors to dog bites and unsafe property conditions, the physical, emotional, and financial toll of personal injury is felt in homes and hospitals across the Phoenix metro area every day. This includes folks in Mesa, Gilbert, Chandler, Glendale, Ahwatukee, Peoria, Tempe, Scottsdale and Paradise Valley.</p>
    <p class="abs center" style="width:100%;top:124px;font-size:6.6px;color:#333">Contact our Phoenix personal injury attorneys today for a <span class="link">free consultation</span> and begin your path to justice and recovery.</p>
    <div class="card" style="left:47px;top:147px;background:linear-gradient(160deg,#7b6e5e,#3a3530)" role="img" aria-label="Worker in a hard hat lying on the floor after a fall"><span>Slip-and-Fall Accidents</span></div>
    <div class="card" style="left:202px;top:147px;background:linear-gradient(160deg,#9aa8b8,#3d4652)" role="img" aria-label="Damaged car after a collision"><span>Car Accidents</span></div>
    <div class="card" style="left:357px;top:147px;background:linear-gradient(160deg,#b5a090,#4d4540)" role="img" aria-label="Doctor's hands with pill bottles"><span>Medical Malpractice</span></div>
    <div class="card" style="left:47px;top:270px;background:linear-gradient(160deg,#8b8176,#33302d)" role="img" aria-label="Injured man in front of a burning building"><span>Catastrophic Injuries</span></div>
    <div class="card" style="left:202px;top:270px;background:linear-gradient(160deg,#8f9a6e,#3f4330)" role="img" aria-label="Dog attacking a person's protected arm"><span>Dog Bites</span></div>
    <div class="card" style="left:357px;top:270px;background:linear-gradient(160deg,#c98a55,#4a3325)" role="img" aria-label="Wrecked red truck on a road at dusk"><span>Wrongful Death</span></div>
  </section>

  <section class="partner">
    <svg class="abs" style="left:0;top:0" width="552" height="410" viewBox="0 0 552 410">
      <path d="M0 40 Q276 -20 552 40 L552 375 Q276 430 0 375Z" fill="#eeeff2"/>
    </svg>
    <h2 class="h abs center" style="width:100%;top:42px;font-size:12.5px">Partnering with a Personal Injury <span class="lt">Lawyer in Phoenix</span></h2>
    <p class="p abs center" style="left:68px;top:72px;width:416px">Corwist Lane is here to serve as your dedicated ally in personal injury law throughout the Valley of the Sun. We understand the chaos and stress accidents bring to your life. But don't worry: we've successfully navigated uncertain times like yours with thousands of satisfied injury clients. We're ready to win peace of mind for you and your loved ones.</p>
    <div class="steps-list">
      <div class="step"><span class="ic"></span>Initial Consultation</div>
      <div class="step"><span class="ic"></span>Case Investigation</div>
      <div class="step"><span class="ic"></span>Settlement Negotiations</div>
      <div class="step active"><span class="ic"></span><div>Litigation<small>Should your case advance to court, our Phoenix personal injury lawyers will relentlessly pursue your rights.</small></div></div>
      <div class="step" style="border-bottom:0"><span class="ic"></span>Resolution</div>
    </div>
    <h3 class="h abs" style="left:279px;top:118px;font-size:10.5px">Litigation</h3>
    <p class="p abs" style="left:279px;top:135px;width:226px">Should your case advance to court, our Phoenix personal injury lawyers will relentlessly pursue your rights. We'll champion your cause to get you the best possible outcome.</p>
    <div class="ph" style="left:275px;top:185px;width:229px;height:147px;background:linear-gradient(135deg,#2d3442,#6a6558 60%,#a08a62)" role="img" aria-label="Lawyers reviewing documents beside a brass scale of justice"></div>
    <p class="abs center" style="left:100px;top:357px;width:352px;font-size:6.6px;line-height:1.8;color:#333">We're available 24/7 for a <span class="link">no-cost consultation</span>. Discover how Phoenix's finest personal injury lawyers can help you seek justice today.</p>
  </section>

  <section class="faq">
    <h2 class="h abs center" style="width:100%;top:53px;font-size:12.5px">FAQs: <span class="lt">Phoenix Personal Injury Lawyers</span></h2>
    <p class="p abs center" style="left:68px;top:83px;width:416px">No two cases are the same, and no two cases should be handled the same way. That said, although this is not legal advice, below are a few general principles that apply to personal injury legal claims in Phoenix, Arizona.</p>
    <div class="pill" style="left:47px;top:117px">When should I speak with my insurance company? What if the other driver's insurance company contacts me?</div>
    <div class="pill" style="left:283px;top:117px">How much does it cost to hire a personal injury lawyer?</div>
    <div class="pill" style="left:47px;top:158px">How much does it cost to have you investigate my personal injury legal claim?</div>
    <div class="pill" style="left:283px;top:158px">How long will it take to recover compensation from my personal injury lawsuit?</div>
    <div class="pill" style="left:47px;top:199px">What steps are involved in bringing a personal injury legal claim?</div>
    <div class="pill" style="left:283px;top:199px">How much money is my personal injury claim worth?</div>
    <div class="btn" style="left:249px;top:245px;width:55px;height:19px">View More</div>
  </section>
</div>

<!-- ================= RIGHT COLUMN ================= -->
<div class="col col-right">
  <section class="faq" style="height:290px">
    <h2 class="h abs center" style="width:100%;top:28px;font-size:12.5px">FAQs: <span class="lt">Phoenix Personal Injury Lawyers</span></h2>
    <p class="p abs center" style="left:68px;top:58px;width:416px">No two cases are the same, and no two cases should be handled the same way. That said, although this is not legal advice, below are a few general principles that apply to personal injury legal claims in Phoenix, Arizona.</p>
    <div class="pill" style="left:47px;top:93px">When should I speak with my insurance company? What if the other driver's insurance company contacts me?</div>
    <div class="pill" style="left:283px;top:93px">How much does it cost to hire a personal injury lawyer?</div>
    <div class="pill" style="left:47px;top:134px">How much does it cost to have you investigate my personal injury legal claim?</div>
    <div class="pill" style="left:283px;top:134px">How long will it take to recover compensation from my personal injury lawsuit?</div>
    <div class="pill" style="left:47px;top:175px">What steps are involved in bringing a personal injury legal claim?</div>
    <div class="pill" style="left:283px;top:175px">How much money is my personal injury claim worth?</div>
    <div class="btn" style="left:248px;top:220px;width:55px;height:19px">View More</div>
  </section>

  <section class="consult">
    <svg class="abs" style="left:0;top:0" width="552" height="210" viewBox="0 0 552 210">
      <path d="M0 22 Q276 -8 552 22 L552 172 Q276 240 0 172Z" fill="#1b56a5"/>
    </svg>
    <h2 class="h abs center" style="width:100%;top:25px;font-size:12.5px;color:#fff">Free Consultation - Start Here</h2>
    <p class="abs center" style="width:100%;top:66px;font-size:6.8px;color:#e4ecf7">Have You Been Seriously Injured in an Phoenix Accident?</p>
    <div class="cstat" style="left:64px"><span class="ring"></span>99% Success Rate</div>
    <div class="cstat" style="left:203px"><span class="ring"></span>550+ 5-Star Reviews</div>
    <div class="cstat" style="left:352px"><span class="ring"></span>$0 Fee Unless We Win</div>
    <div class="btn btn-ghost" style="left:243px;top:136px;width:66px;height:20px">Free Case Review</div>
  </section>

  <section class="firm">
    <h2 class="h abs center" style="width:100%;top:35px;font-size:12.5px">An Injury Law Firm <span class="lt">That Puts Phoenix First</span></h2>
    <p class="p abs center" style="left:68px;top:67px;width:416px">Our founder, Daniel Corwist, was born and raised in the Valley of the Sun. He grew up in Phoenix and graduated from Ridgeline High School, just off Route 51, above the Phoenix Mountains Preserve. Now named a top lawyer by Valley Monthly, Mr. Corwist is proud to serve his hometown with his personal injury expertise.</p>
    <div class="bio"></div>
    <div class="circle-img" style="left:88px;top:108px;width:76px;height:76px;border-color:#fff;background:linear-gradient(160deg,#c9ccd0,#5a6470)" role="img" aria-label="Portrait of founding attorney Daniel R. Corwist"></div>
    <div class="abs center" style="left:70px;top:190px;width:116px;font-size:9px;color:var(--blue);font-weight:600">DANIEL R. CORWIST</div>
    <div class="abs center" style="left:70px;top:205px;width:116px;font-size:6px;color:#333">Attorney, Director</div>
    <div class="tag" style="left:202px;top:136px">EDUCATION</div>
    <div class="abs" style="left:202px;top:160px;font-size:5.8px;line-height:1.9;color:#333"><b>Eastbrook University School of Law</b><br>J.D. – 1991<br><b>Desert State University</b><br>B.A., General Studies – 1988<br>Honors: cum laude</div>
    <div class="tag" style="left:339px;top:136px">POPULAR POSTS BY MR. CORWIST</div>
    <div class="abs" style="left:341px;top:162px;width:140px;font-size:5.8px;line-height:1.8;color:#333">I Feel Fine; Should I Still See A Doctor After My Automobile Accident?<br><br>Should I release my medical records to another driver's insurance adjuster?</div>
  </section>

  <section class="named">
    <h2 class="h abs" style="left:47px;top:36px;font-size:12.5px;line-height:1.4">Named a Top Personal Injury<br>Lawyer in Phoenix</h2>
    <div class="abs" style="left:47px;top:86px;font-family:'Oswald',sans-serif;font-size:8.5px;color:#222">By Valley Monthly</div>
    <p class="p abs" style="left:47px;top:103px;width:205px">Named a Top Lawyer by Valley Monthly. Our founder, Daniel Corwist, is not just a name in Phoenix's legal circles; he's a force to be reckoned with. Daniel embodies the passion, persistence and experience that separates Corwist Lane Injury Lawyers from the rest of the pack. With over 30 years in personal injury law, he has proven to maximize his clients recovery – and set new standards. In addition, Corwist is home-grown; he grew up in Phoenix, and graduated from Ridgeline High School in 1984.</p>
    <div class="ph" style="left:283px;top:43px;width:104px;height:105px;background:#3a3a3a" role="img" aria-label="Top lawyer award badge"></div>
    <div class="ph" style="left:395px;top:45px;width:100px;height:100px;border-radius:50%;background:radial-gradient(circle,#d8a848,#8a5a1e)" role="img" aria-label="National top personal injury team award seal"></div>
    <p class="abs center" style="left:283px;top:163px;width:215px;font-size:5.8px;line-height:1.8;color:#333">As recognized by <i class="link" style="font-weight:700">Counsel Review Magazine</i> — ranked the #1 personal injury team in the U.S.</p>
  </section>

  <section class="roadmap">
    <h2 class="h abs center" style="width:100%;top:37px;font-size:12.5px;line-height:1.5">The Steps Corwist Lane Injury Lawyers Will Take In Your<br><span class="lt">Phoenix Personal Injury Case</span></h2>
    <p class="p abs center" style="left:60px;top:90px;width:432px">When you're dealing with a personal injury claim, the legal world can seem complicated. At Corwist Lane Injury Lawyers, we make it simpler for you. As your dedicated Phoenix personal injury attorneys, we break down the process into clear, easy-to-follow steps – a "roadmap". Here's how we support you:</p>
    <svg class="abs" style="left:0;top:150px" width="552" height="130" viewBox="0 0 552 130">
      <g fill="none" stroke="#555" stroke-width="1" stroke-dasharray="3 3">
        <path d="M106 65 L106 25 Q106 10 124 10 Q146 10 146 25 L146 100 Q146 120 166 120 Q186 120 186 100 L186 65"/>
        <path d="M215 65 L262 65"/>
        <path d="M280 65 L280 25 Q280 10 298 10 Q318 10 318 25 L318 100 Q318 120 338 120 Q358 120 358 100 L358 65"/>
        <path d="M385 65 L430 65"/>
      </g>
    </svg>
    <div class="rm-ring" style="left:83px;top:192px"></div>
    <div class="rm-ring blue" style="left:167px;top:192px"></div>
    <div class="rm-ring" style="left:256px;top:192px"></div>
    <div class="rm-ring blue" style="left:340px;top:192px"></div>
    <div class="rm-ring" style="left:423px;top:192px"></div>
    <div class="rm-label" style="left:150px;top:145px">Preserving Vital Evidence for Your Case</div>
    <div class="rm-label" style="left:323px;top:145px">Keeping You in the Loop with Constant Availability</div>
    <div class="rm-label" style="left:66px;top:246px">Handling All Communications Related to Your Personal Injury Case</div>
    <div class="rm-label" style="left:239px;top:246px">Comprehensive Investigation of Accident Information</div>
    <div class="rm-label" style="left:406px;top:246px">Candid Communication — the Straight Scoop</div>
  </section>

  <section class="serving">
    <div class="abs" style="left:75px;top:40px;width:162px;height:162px;border-radius:50%;background:#c9d7ea"></div>
    <div class="circle-img" style="left:68px;top:48px;width:152px;height:152px;background:linear-gradient(150deg,#8fa0b4,#3a4658)" role="img" aria-label="Three attorneys walking together outside an office building"></div>
    <h2 class="h abs" style="left:285px;top:38px;font-size:12.5px;line-height:1.5">Serving Phoenix and the Entire Valley<br><span class="lt">with Trusted Personal Injury<br>Representation</span></h2>
    <p class="p abs" style="left:285px;top:95px;width:212px">At Corwist Lane Injury Lawyers, we're proud to represent individuals and families across the entire Phoenix metro area. Whether you're in Scottsdale, Mesa, Glendale, Chandler, Gilbert, Peoria, or Paradise Valley, our personal injury attorneys are ready to help you fight for the justice and compensation you deserve. We understand how overwhelming it can be to deal with an injury — especially when you're facing medical bills, time away from work, or insurance companies that won't play fair.</p>
    <div class="btn" style="left:285px;top:196px;width:50px;height:19px">Read More</div>
    <h2 class="h abs" style="left:47px;top:256px;font-size:12.5px;line-height:1.5">Why You Need a Phoenix, Arizona<br><span class="lt">Personal Injury Lawyer Versus an<br>Out-Of-State Lawyer?</span></h2>
    <p class="p abs" style="left:47px;top:313px;width:205px">If you've been involved in any type of accident in Phoenix or any other city in Arizona, hiring a local Phoenix personal injury attorney is crucial for so many reasons. Here are a few: Personal injury laws vary from state to state and even from city to city. That's why it is so important to hire a Phoenix, Arizona personal injury lawyer, who works and lives in Phoenix, Arizona. The personal injury attorney in Phoenix will be familiar with state-specific statutes and regulations.</p>
    <div class="btn" style="left:47px;top:404px;width:50px;height:19px">Read More</div>
    <div class="abs" style="left:286px;top:240px;width:162px;height:162px;border-radius:50%;background:#c9d7ea"></div>
    <div class="circle-img" style="left:304px;top:258px;width:152px;height:152px;background:linear-gradient(150deg,#a39b87,#3b3834)" role="img" aria-label="Couple sitting together looking concerned in their living room"></div>
  </section>

  <section class="case">
    <h2 class="h abs center" style="width:100%;top:33px;font-size:12.5px">Do You Have <span class="lt">a Case?</span></h2>
    <div class="field" style="left:96px;top:73px;width:176px">Name</div>
    <div class="field" style="left:279px;top:73px;width:176px">Email</div>
    <div class="field" style="left:96px;top:100px;width:176px">Phone Number</div>
    <div class="field" style="left:279px;top:100px;width:176px">Case Type</div>
    <div class="field" style="left:96px;top:127px;width:359px;height:36px">Message</div>
    <div class="btn" style="left:225px;top:180px;width:102px;height:20px">Get your Free Case Review</div>
  </section>

  <section class="footer">
    <div class="abs brand" style="left:48px;top:33px">
      <span class="brand-dot" style="width:16px;height:16px;background:#fff"></span>
      <div><div class="brand-name" style="color:#fff;font-size:10px">CORWIST LANE</div><div class="brand-sub" style="color:#bbb;font-size:4px">INJURY LAWYERS</div></div>
    </div>
    <div class="abs" style="left:66px;top:63px;display:flex;gap:5px">
      <span style="width:11px;height:11px;border-radius:50%;background:var(--blue)"></span>
      <span style="width:11px;height:11px;border-radius:50%;border:1px solid #fff"></span>
      <span style="width:11px;height:11px;border-radius:50%;border:1px solid #fff"></span>
      <span style="width:11px;height:11px;border-radius:50%;border:1px solid #fff"></span>
    </div>
    <div class="fcol abs" style="left:171px;top:32px"><h5>Quick Links</h5><ul><li>Home</li><li>Phoenix</li><li>Denver</li><li>Tucson</li><li>Disclaimer</li><li>Privacy Policy</li><li>Sitemap</li></ul></div>
    <div class="fcol abs" style="left:258px;top:32px"><h5>Other Links</h5><ul><li>Car Accidents</li><li>Truck &amp; Tractor-Trailer Accidents</li><li>Wrongful Death</li><li>Premises Liability – Slip &amp; Fall</li><li>Motorcycle Accidents</li><li>Pedestrian Accidents</li><li>Dog Bite</li><li>Bus Accidents</li><li>Defective Products</li></ul></div>
    <div class="fcol abs" style="left:395px;top:32px;width:125px">
      <h5>Contact Us</h5>
      <div class="contact-row"><i></i><span>Corwist Lane Injury Lawyers<br>Phoenix Office</span></div>
      <div class="contact-row"><i></i><span>1180 E Saguaro Ave #400<br>Phoenix, AZ 85016</span></div>
      <div class="contact-row"><i></i><span>602-555-0148</span></div>
    </div>
    <div class="abs" style="left:48px;top:200px;width:456px;height:1px;background:#444"></div>
    <p class="abs center" style="width:100%;top:214px;font-size:5.8px;color:#ccc">© 2025 by Corwist Lane Injury Lawyers™. All rights reserved. A division of Halbrook Ardent.</p>
  </section>
</div>

</div>
</body>
</html>
```